Hi Designers,

I will need 4 web pages designed. The web page looks like an App (if you click on the logo, or the icon on an iPad, it will take you to the website), but it is still a webpage.

Please check the attachment on this brief to understand what specific pages I need to be designed.

A .PSD (straight-up PhotoShop image) as final deliverable is fine, as long as you give us the exact “web color numbers”.

The design is for desktop and iPad but in a single unified web application, NOT separate web app and (native) iPad app.

Details:

Brightwell Ledger Advisory Group is developing a browser-based application for use on any mobile device or desktop. The app will be used by corporations to communicate with their employees regarding legal, regulatory and company requirements for conducting business. The app is known as “Harbor Rulebook Hub.” When the user clicks on the icon for Harbor Rulebook Hub, they will enter a site full of information that a company deems necessary for the employee to do his/her job. There are several content sections within the site, including a login page, training, policies, forms, news feeds and blogs.

The application has been built using Microsoft .NET, and fully supports CSS-type skinning; it uses traditional page layouts. We are seeking a product logo concept (image), a master application/desktop icon (image), as well as a full color scheme/theme/skin design for all areas of the application (header area, body text, menu bar, etc.) in the form of a CSS. The look should be clean, crisp and professional; nothing cartoony or whimsical. It should be easy to read and “airy”.

We have sketched prototypes for the basic application page layout that we can send as a next step of the process.
Updates

Screen shots have been uploaded to this project.  Please use them to guide your design.

Dear designers,

I apologize for the delay in providing feedback. My partners and I will provide feedback in a few days. Thank you for your patience.

Industry/Entity Type

Business

Font styles to use
Other font styles liked:
• see font on screen shots when uploaded

```html
<!DOCTYPE html>
<html lang="en">
<head>
<meta charset="utf-8">
<title>Harbor Rulebook Hub – Sign In and Home</title>
<link rel="stylesheet" href="https://fonts.googleapis.com/css2?family=Open+Sans:wght@400;600;700&display=swap">
<style>
  :root {
    --page-bg: #ffffff;
    --header-navy: #0a2c55;
    --header-line: #14406f;
    --body-navy: #063868;
    --body-glow: #3a77b0;
    --text-light: #ffffff;
    --text-soft: #e6eef7;
    --tile-top: #ffffff;
    --tile-bottom: #dcdcdc;
    --tile-text: #333333;
    --icon-dark: #2e2e2e;
    --go-green-top: #9fd64a;
    --go-green-bottom: #6fae1f;
    --field-top: #ffffff;
    --field-bottom: #e9e9e9;
  }
  * { box-sizing: border-box; margin: 0; padding: 0; }
  html, body {
    width: 1200px; height: 1094px; overflow: hidden;
    background: var(--page-bg);
    font-family: "Open Sans", Arial, sans-serif;
  }
  .screen {
    position: absolute; top: 282px; width: 394px; height: 568px;
    overflow: hidden;
    background: radial-gradient(ellipse 200px 190px at 198px 255px, var(--body-glow) 0%, #1d548c 45%, var(--body-navy) 100%);
  }
  .screen--signin { left: 137px; }
  .screen--home { left: 676px; background: radial-gradient(ellipse 230px 200px at 198px 250px, #245d96 0%, var(--body-navy) 75%); }

  .app-header {
    position: absolute; left: 0; top: 0; width: 100%; height: 53px;
    background: var(--header-navy);
    border-bottom: 1px solid var(--header-line);
    color: var(--text-light);
  }
  .brand {
    position: absolute; left: 16px; top: 0; height: 53px;
    display: flex; align-items: center; gap: 10px;
    font-size: 13px; font-weight: 400; color: var(--text-soft);
  }
  .brand-mark { width: 32px; height: 32px; border-radius: 50%; background: #2f7fc1; }
  .product-name {
    position: absolute; right: 13px; top: 0; line-height: 53px;
    font-size: 13px; font-weight: 700;
  }

  .signin-form { position: absolute; left: 29px; top: 170px; width: 335px; color: var(--text-soft); }
  .field-label { display: block; font-size: 15px; margin-bottom: 7px; }
  .field {
    display: block; width: 335px; height: 38px; margin-bottom: 16px;
    background: linear-gradient(var(--field-top) 55%, var(--field-bottom));
    border: 1px solid #cfd6de; border-radius: 2px;
  }
  .signin-links { font-size: 15px; margin-top: 8px; }
  .signin-links .divider { margin: 0 7px; }
  .signin-button {
    margin-top: 19px; width: 94px; height: 38px; border: none; border-radius: 2px;
    background: linear-gradient(var(--go-green-top), var(--go-green-bottom));
    color: var(--text-light); font: 400 14px "Open Sans", Arial, sans-serif;
    display: flex; align-items: center; justify-content: center; gap: 6px;
  }

  .back-button {
    position: absolute; left: 22px; top: 13px; height: 27px;
    display: flex; align-items: center;
  }
  .back-button .label {
    height: 27px; line-height: 27px; padding: 0 8px 0 4px;
    background: linear-gradient(#ffffff, #d8d8d8);
    color: #222; font-size: 13px; font-weight: 600; border-radius: 0 2px 2px 0;
  }
  .user-menu { position: absolute; right: 22px; top: 0; line-height: 56px; font-size: 14px; font-weight: 700; }

  .tile {
    position: absolute; width: 166px; height: 81px;
    background: linear-gradient(var(--tile-top) 40%, var(--tile-bottom));
    border-radius: 2px; box-shadow: 0 1px 2px rgba(0,0,0,.35);
    display: flex; align-items: center; gap: 12px; padding-left: 16px;
    color: var(--tile-text); font-size: 15px; line-height: 20px;
  }
  .tile svg { width: 44px; height: 44px; flex: none; fill: var(--icon-dark); }
  .col-a { left: 24px; } .col-b { left: 204px; } .col-mid { left: 116px; }
  .row-1 { top: 128px; } .row-2 { top: 222px; } .row-3 { top: 315px; } .row-4 { top: 408px; }
</style>
</head>
<body>

<section class="screen screen--signin" aria-label="Sign in">
  <header class="app-header">
    <div class="brand"><span class="brand-mark"></span>Corvane Labs</div>
    <div class="product-name">Harbor Rulebook Hub</div>
  </header>
  <form class="signin-form">
    <label class="field-label">Username</label>
    <span class="field"></span>
    <label class="field-label">Password</label>
    <span class="field"></span>
    <p class="signin-links">Keep me signed in<span class="divider">|</span>Forgot Password?</p>
    <button class="signin-button" type="button">
      <svg width="11" height="14" viewBox="0 0 11 14"><path d="M2.5 6V4a3 3 0 0 1 6 0v2" fill="none" stroke="#fff" stroke-width="1.6"/><rect x="0.5" y="6" width="10" height="8" rx="1" fill="#fff"/></svg>
      Sign In
    </button>
  </form>
</section>

<section class="screen screen--home" aria-label="Home">
  <header class="app-header">
    <div class="back-button">
      <svg width="12" height="27" viewBox="0 0 12 27"><path d="M12 0 0 13.5 12 27Z" fill="#ececec"/></svg>
      <span class="label">Home</span>
    </div>
    <div class="user-menu">Marcus ▾</div>
  </header>

  <div class="tile col-a row-1">
    <svg viewBox="0 0 44 44"><path d="M4 6h36v32H4Z M7 9v26h30V9Z"/><rect x="10" y="12" width="24" height="4"/><rect x="10" y="19" width="10" height="12"/><rect x="23" y="19" width="11" height="3"/><rect x="23" y="24" width="11" height="3"/><rect x="23" y="29" width="8" height="2"/></svg>
    <span>Compliance<br>News</span>
  </div>
  <div class="tile col-b row-1">
    <svg viewBox="0 0 44 44"><circle cx="13" cy="31" r="6" fill="none" stroke="#2e2e2e" stroke-width="4"/><path d="M7 10v21h4V10Z"/><path d="M20 15a14 14 0 0 1 14 14h-4a10 10 0 0 0-10-10Z"/><path d="M20 5a24 24 0 0 1 24 24h-4A20 20 0 0 0 20 9Z"/></svg>
    <span>Compliance<br>Blog</span>
  </div>
  <div class="tile col-a row-2">
    <svg viewBox="0 0 44 44"><circle cx="22" cy="22" r="20"/><path d="M16 17a6 6 0 1 1 9 5c-2 1-3 2-3 4v1" fill="none" stroke="#fff" stroke-width="4.5"/><circle cx="22" cy="33" r="2.6" fill="#fff"/></svg>
    <span>FAQ’s</span>
  </div>
  <div class="tile col-b row-2">
    <svg viewBox="0 0 44 44"><path d="M8 8a5 5 0 0 1 5-5h23v30H13a2 2 0 0 0 0 4h23v4H13a6 6 0 0 1-5-6Z"/><path d="M18 8h12v12l-6-4-6 4Z" fill="#fff"/></svg>
    <span>Document<br>Library</span>
  </div>
  <div class="tile col-a row-3">
    <svg viewBox="0 0 44 44"><g fill="none" stroke="#2e2e2e" stroke-width="5"><path d="M19 13l5-5a7 7 0 0 1 10 10l-5 5"/><path d="M25 31l-5 5a7 7 0 0 1-10-10l5-5"/><path d="M16 28 28 16"/></g></svg>
    <span>Relevant<br>Links</span>
  </div>
  <div class="tile col-b row-3">
    <svg viewBox="0 0 44 44"><path d="M16 3h17l7 7v24H16Z"/><path d="M19 7h12v5h5v19H19Z" fill="#fff"/><rect x="22" y="15" width="11" height="2"/><rect x="22" y="20" width="11" height="2"/><path d="M4 13h17v28H4Z"/><path d="M7 16h11v22H7Z" fill="#fff"/><rect x="8" y="30" width="2" height="7"/><rect x="11" y="26" width="2" height="11"/><rect x="14" y="28" width="2" height="9"/></svg>
    <span>Reports</span>
  </div>
  <div class="tile col-mid row-4">
    <svg viewBox="0 0 44 44"><rect x="2" y="2" width="40" height="40" rx="3"/><rect x="10" y="9" width="10" height="10" fill="#fff"/><circle cx="29" cy="14" r="5" fill="#fff"/><path d="M15 25l6 10H9Z" fill="#fff"/><rect x="24" y="25" width="10" height="10" rx="3" fill="#fff"/></svg>
    <span>Forms</span>
  </div>
</section>

</body>
</html>
```